Webdesign for silver path

"Der Sternenpfad" is a new info product that will be selled through the website maybe you will create for us.

Translated from german to english the project is named "the silver path". It´s an online video course that teaches people how to live a fulfilling, happy and healthy life.

Design paramaters
We want a serious design that embodies the real feeling of beeing happy and fulfilled. Visitors should even feel good/better when they see the website.
In color psychology some sort of calming deep green like a four-leaf clover is recommend.
Mainly the website will be the external sales page with a big video as the central attention.
We also need a member area for customers to watch our video course.

So mainly we need a eye-cathing, calming header, the content body with mainly video and just a few written words...and of course a footer for links like imprint, affiliate program etc.

What we not want:
- some kind of these exaggerated smiling photos
- that bathetic luck symbols like money or boats
Updates

Hi,

i posted a message to the design discussion. Thank you!

Industry/Entity Type

Affiliate

```html
<!DOCTYPE html>
<html lang="en">
<head>
<meta charset="utf-8">
<title>Der Sternenpfad</title>
<link href="https://fonts.googleapis.com/css2?family=Lato:wght@400;700&display=swap" rel="stylesheet">
<style>
:root{
  --ink:#333333;
  --muted:#666666;
  --light:#888888;
  --white:#ffffff;
  --green-top:#8abb15;
  --green-mid:#3f9420;
  --green-bottom:#0b6b26;
  --nav-top:#6aa514;
  --btn-top:#3fa23a;
  --btn-bottom:#11701d;
  --field:#e8e8e8;
  --field-line:#b9b9b9;
  --footer:#ebebeb;
  --rule:#cccccc;
  --board:#aab6b2;
}
*{margin:0;padding:0;box-sizing:border-box}
html,body{width:1200px;height:1171px;overflow:hidden;background:var(--white)}
body{font-family:"Lato",Arial,sans-serif;color:var(--ink);position:relative}
.abs{position:absolute}

.site-header{position:absolute;left:0;top:0;width:1200px;height:110px;background:var(--white)}
.brand{left:55px;top:38px;font-size:33px;letter-spacing:.5px;color:var(--ink);text-transform:uppercase}
.login-label{left:574px;top:48px;font-size:18px;color:var(--muted)}
.field{height:33px;width:214px;top:42px;background:var(--field);border:1px solid var(--field-line);border-radius:4px;font-size:11.5px;color:#a0a0a0;padding:12px 0 0 12px;letter-spacing:.3px}
.field.user{left:630px}
.field.pass{left:855px}
.login-btn{left:1075px;top:42px;width:67px;height:33px;border-radius:4px;background:linear-gradient(var(--btn-top),var(--btn-bottom));color:var(--white);font-size:15px;text-align:center;line-height:32px;border:1px solid #0e5f18}
.remember{left:631px;top:84px;font-size:12px;color:var(--light);display:flex;align-items:center;gap:5px}
.checkbox{width:12px;height:12px;border:1px solid #999;background:var(--white);border-radius:2px}
.forgot{left:860px;top:84px;font-size:12px;color:var(--light)}

.hero{position:absolute;left:0;top:110px;width:1200px;height:461px;background:linear-gradient(var(--green-top) 0%,var(--green-mid) 55%,var(--green-bottom) 100%)}
.main-nav{position:absolute;left:51px;top:0;width:1094px;height:55px;background:linear-gradient(var(--nav-top),rgba(120,180,20,0))}
.nav-item{position:absolute;top:14px;font-size:16px;color:var(--white)}
.nav-item.active{left:11px;top:13px;width:85px;height:30px;border:1px solid #e6f5b0;border-radius:4px;background:linear-gradient(#b5d83a,#8cbf1c);color:#1d5e0d;text-align:center;line-height:28px}
.nav-sep{position:absolute;top:16px;width:1px;height:24px;background:rgba(255,255,255,.35)}

.hero-title{left:78px;top:114px;font-size:29px;color:var(--white);line-height:34px}
.hero-sub{left:78px;top:148px;font-size:24px;color:var(--white)}
.hero-text{left:80px;top:199px;width:430px;font-size:13.6px;line-height:20px;color:var(--white)}
.learn-btn{left:82px;top:336px;width:117px;height:28px;border:1px solid #e8f5df;border-radius:4px;background:#3aa152;color:#0f4f18;font-size:14px;text-align:center;line-height:26px}

.video-frame{left:579px;top:78px;width:527px;height:337px;background:#4f9a3f;box-shadow:0 22px 22px -14px rgba(0,40,10,.55)}
.video-screen{left:5px;top:6px;width:516px;height:326px;background:linear-gradient(135deg,#b3bfbb,var(--board) 60%,#97a4a0)}
.video-controls{left:14px;top:279px;width:490px;height:34px;background:rgba(235,240,238,.45);border-radius:4px}

.welcome{position:absolute;left:78px;top:604px;width:1040px}
.welcome h1{font-weight:400;font-size:29px;color:var(--ink);margin-bottom:10px}
.welcome p{font-size:14.3px;line-height:21.2px;color:var(--ink);margin-bottom:12px}

.site-footer{position:absolute;left:0;top:954px;width:1200px;height:217px;background:var(--footer)}
.footer-col{position:absolute;top:33px;list-style:none;font-size:13px;color:var(--muted)}
.footer-col li{height:24.5px}
.footer-brand{left:890px;top:74px;font-size:22px;color:#777;text-transform:uppercase}
.footer-rule{left:50px;top:171px;width:1095px;height:1px;background:var(--rule)}
.legal{right:88px;top:186px;font-size:11.5px;color:var(--light)}
</style>
</head>
<body>
<header class="site-header">
  <div class="abs brand">Der Sternenpfad</div>
  <div class="abs login-label">Login</div>
  <div class="abs field user">USERNAME</div>
  <div class="abs field pass">PASSWORD</div>
  <div class="abs login-btn">Login</div>
  <div class="abs remember"><span class="checkbox"></span>Remember Me</div>
  <div class="abs forgot">Forgot Password?</div>
</header>

<section class="hero">
  <nav class="main-nav">
    <div class="nav-item active">Home</div>
    <div class="nav-item" style="left:122px">About Us</div>
    <div class="nav-sep" style="left:214px"></div>
    <div class="nav-item" style="left:238px">Why Choose Us</div>
    <div class="nav-sep" style="left:376px"></div>
    <div class="nav-item" style="left:399px">Videos</div>
    <div class="nav-sep" style="left:473px"></div>
    <div class="nav-item" style="left:496px">Blog</div>
    <div class="nav-sep" style="left:554px"></div>
    <div class="nav-item" style="left:577px">Services</div>
    <div class="nav-sep" style="left:659px"></div>
    <div class="nav-item" style="left:684px">Contact Us</div>
    <div class="nav-sep" style="left:789px"></div>
  </nav>

  <div class="abs hero-title">Welcome To Der Sternenpfad</div>
  <div class="abs hero-sub">Title Comes Here</div>
  <p class="abs hero-text">Lorem Ipsum is simply dummy text of the printing and typesetting industry. Lorem Ipsum has been the industry's standard dummy text ever since the 1500s, when an unknown printer took a galley of type and scrambled it to make a type specimen book. It has survived not only five centuries, but also the leap into electronic typesetting, remaining essentially unchanged.</p>
  <div class="abs learn-btn">Learn More</div>

  <div class="abs video-frame">
    <div class="abs video-screen" role="img" aria-label="Course video still: a lesson written on a whiteboard">
      <svg class="abs" style="left:238px;top:138px" width="32" height="36" viewBox="0 0 32 36"><polygon points="2,2 30,18 2,34" fill="rgba(255,255,255,.75)"/></svg>
      <div class="abs video-controls">
        <svg width="490" height="34" viewBox="0 0 490 34">
          <polygon points="12,10 24,17 12,24" fill="#fff"/>
          <rect x="36" y="10" width="4" height="14" fill="#fff"/><rect x="43" y="10" width="4" height="14" fill="#fff"/>
          <rect x="58" y="11" width="12" height="12" fill="#fff"/>
          <line x1="80" y1="17" x2="426" y2="17" stroke="#fff" stroke-width="2"/>
          <circle cx="84" cy="17" r="4" fill="#fff"/>
          <rect x="448" y="20" width="3" height="5" fill="#aaa"/><rect x="453" y="17" width="3" height="8" fill="#aaa"/><rect x="458" y="14" width="3" height="11" fill="#aaa"/><rect x="463" y="11" width="3" height="14" fill="#aaa"/>
        </svg>
      </div>
    </div>
  </div>
</section>

<main class="welcome">
  <h1>Welcome!</h1>
  <p>Lorem Ipsum is simply dummy text of the printing and typesetting industry. Lorem Ipsum has been the industry's standard dummy text ever since the 1500s, when an unknown printer took a galley of type and scrambled it to make a type specimen book. It has survived not only five centuries, but also the leap into electronic typesetting, remaining essentially unchanged. Lorem Ipsum is simply dummy text of the printing and typesetting industry. Lorem Ipsum has been the industry's standard dummy text ever since the 1500s, when an unknown printer took a galley of type and scrambled it to make a type specimen book. It has survived not only five centuries, but also the leap into electronic typesetting, remaining essentially unchanged.</p>
  <p>Lorem Ipsum is simply dummy text of the printing and typesetting industry. Lorem Ipsum has been the industry's standard dummy text ever since the 1500s, when an unknown printer took a galley of type and scrambled it to make a type specimen book. It has survived not only five centuries, but also the leap into electronic typesetting, remaining essentially unchanged.</p>
  <p>Lorem Ipsum is simply dummy text of the printing and typesetting industry. Lorem Ipsum has been the industry's standard dummy text ever since the 1500s, when an unknown printer took a galley of type and scrambled it to make a type specimen book. It has survived not only five centuries, but also the leap into electronic typesetting, remaining essentially unchanged.</p>
</main>

<footer class="site-footer">
  <ul class="footer-col" style="left:81px"><li>Home</li><li>About Us</li><li>Why Choose Us</li><li>Videos</li><li>Recent Blog</li></ul>
  <ul class="footer-col" style="left:277px"><li>Blog</li><li>Services</li><li>Support</li><li>Join Our Course</li><li>Careers</li></ul>
  <ul class="footer-col" style="left:456px"><li>Testimonials</li><li>News</li><li>FAQ</li><li>Contact Us</li></ul>
  <div class="abs footer-brand">Der Sternenpfad</div>
  <div class="abs footer-rule"></div>
  <div class="abs legal">© 2012 - Terms of Service - Privacy Policy - Program Policies</div>
</footer>
</body>
</html>
```